Corporate consulting business needs a business card

I want a professional business card.... surprise me

Updates

Reason: i dont think 2 days is enough

Target Market(s)

Corprorate and Not for Profit firms and organisations

Industry/Entity Type

Consulting

Contact Information for Business Card

Logo
Corporate Consulting Services
On Time, On Budget, Beyond Expectation
Tovan Presfield
Director
0427 31 94 62 (Larger)
tovan@tp-advisory.com.au
www.tp-advisory.com.au
include little icons beside the contact info:

- Envelope = email
- Phone = phone
- Globe = website

Font styles to use
Serif
Sans Serif

Requirements
Must have
• Professional and clean
Nice to have
• you tell me

```html
<!DOCTYPE html>
<html lang="en">
<head>
<meta charset="utf-8">
<title>TP Advisory – Business Card</title>
<link rel="stylesheet" href="https://fonts.googleapis.com/css2?family=Cinzel:wght@500&family=Questrial&display=swap">
<style>
  :root{
    --canvas:#ece8e3;
    --brown:#5a2f14;
    --brown-dark:#44220d;
    --brown-light:#6b3a1a;
    --paper:#ffffff;
    --ink:#111111;
    --text-light:#f4ece4;
    --text-soft:#d9c9ba;
  }
  *{box-sizing:border-box;margin:0;padding:0}
  html,body{width:1200px;height:1023px;overflow:hidden;background:var(--canvas)}
  body{position:relative;font-family:"Questrial",sans-serif}

  .card{
    position:absolute;left:250px;width:700px;height:400px;border-radius:28px;overflow:hidden;
    background:linear-gradient(160deg,var(--brown-light),var(--brown) 45%,var(--brown-dark));
    box-shadow:0 14px 30px rgba(60,30,10,.28);
  }
  .card-front{top:80px}
  .card-back{top:543px}

  .front-shapes{position:absolute;inset:0}

  .brand{position:absolute;display:flex;flex-direction:column;align-items:center;gap:14px}
  .brand-mark{width:78px;height:78px;border-radius:50%;border:3px solid var(--brown)}
  .brand-name{font-family:"Cinzel",serif;font-weight:500;font-size:24px;letter-spacing:1px;color:var(--brown)}
  .card-front .brand{left:55px;top:210px}

  .details{position:absolute;right:48px;top:42px;text-align:right;color:var(--text-light)}
  .person-name{font-size:30px;letter-spacing:3px}
  .person-role{font-size:17px;letter-spacing:2px;color:var(--text-soft);margin-top:2px}
  .contact{list-style:none;margin-top:28px;font-size:15px;line-height:1.55}
  .contact li{display:flex;justify-content:flex-end;align-items:center;gap:10px}
  .contact .phone{font-size:19px;letter-spacing:1px}
  .contact svg{width:15px;height:15px;flex:none}
  .services{margin-top:24px;font-size:17px;line-height:1.45}
  .services strong{font-weight:400;letter-spacing:.5px}
  .tagline{color:var(--text-soft);font-size:16px}

  .card-back .brand{left:50%;top:50%;transform:translate(-50%,-50%)}
  .card-back .brand-mark{border-color:var(--text-light);width:96px;height:96px}
  .card-back .brand-name{color:var(--text-light);font-size:28px}
</style>
</head>
<body>

<section class="card card-front">
  <svg class="front-shapes" viewBox="0 0 700 400" aria-hidden="true">
    <path d="M0,18 C190,30 320,190 352,400" fill="none" stroke="var(--ink)" stroke-width="16"/>
    <path d="M0,34 C175,44 300,200 330,400" fill="none" stroke="var(--paper)" stroke-width="3"/>
    <path d="M0,42 C170,52 292,206 322,400" fill="none" stroke="var(--brown)" stroke-width="8"/>
    <path d="M0,52 C165,62 280,210 310,400 L0,400 Z" fill="var(--paper)"/>
  </svg>

  <div class="brand">
    <span class="brand-mark"></span>
    <span class="brand-name">TP ADVISORY</span>
  </div>

  <div class="details">
    <p class="person-name">Tovan Presfield</p>
    <p class="person-role">Director</p>
    <ul class="contact">
      <li class="phone">0427 31 94 62
        <svg viewBox="0 0 16 16"><path fill="currentColor" d="M3.5 1.5l2.5 0 1 3.5-1.7 1.2a8 8 0 0 0 4.5 4.5L11 9l3.5 1v2.5c0 1-1 2-2 2C6.5 14.5 1.5 9.5 1.5 3.5c0-1 1-2 2-2z"/></svg>
      </li>
      <li>tovan@tp-advisory.com.au
        <svg viewBox="0 0 16 16"><rect x="1.5" y="3.5" width="13" height="9" fill="none" stroke="currentColor" stroke-width="1.4"/><path d="M1.5 3.5l6.5 5 6.5-5" fill="none" stroke="currentColor" stroke-width="1.4"/></svg>
      </li>
      <li>www.tp-advisory.com.au
        <svg viewBox="0 0 16 16"><g fill="none" stroke="currentColor" stroke-width="1.3"><circle cx="8" cy="8" r="6.3"/><ellipse cx="8" cy="8" rx="2.8" ry="6.3"/><path d="M1.7 8h12.6M3 4.5h10M3 11.5h10"/></g></svg>
      </li>
    </ul>
    <div class="services">
      <p><strong>Corporate Consulting Services :</strong></p>
      <p class="tagline">On Time,</p>
      <p class="tagline">On Budget,</p>
      <p class="tagline">Beyond Expectation</p>
    </div>
  </div>
</section>

<section class="card card-back">
  <div class="brand">
    <span class="brand-mark"></span>
    <span class="brand-name">TP ADVISORY</span>
  </div>
</section>

</body>
</html>
```